Building Company Business Card Design

I am looking to get a business card designed for my Building Company. Please find the logo attached.

Industry/Entity Type

Business

Contact Information for Business Card

Mobile 0472 913 046
Email admin@tarrowconstructworks.com.au
Website www.tarrowconstructworks.com.au

Colors
0255a3

```html
<!DOCTYPE html>
<html lang="en">
<head>
<meta charset="utf-8">
<title>Tarrow Construct Works – Business Card</title>
<link rel="stylesheet" href="https://fonts.googleapis.com/css2?family=Arimo:wght@400&family=Montserrat:wght@600&display=swap">
<style>
  :root {
    --brand-blue: #0255a3;
    --brand-blue-deep: #024c92;
    --swoosh-grey: #6d6e71;
    --card-white: #ffffff;
    --ink: #2b2b2b;
    --page-bg: #e9e7e3;
  }
  * { margin: 0; padding: 0; box-sizing: border-box; }
  html, body { width: 1200px; height: 900px; overflow: hidden; background: var(--page-bg); }

  .card-slot {
    position: absolute;
    left: 260px;
    width: 680px; height: 401px;
    box-shadow: 0 6px 18px rgba(0,0,0,0.18);
    overflow: hidden;
  }
  .card-slot--back { top: 30px; }
  .card-slot--front { top: 466px; }

  .card-face {
    position: absolute; left: 0; top: 0;
    width: 1000px; height: 590px;
    transform: scale(0.68);
    transform-origin: 0 0;
    overflow: hidden;
    font-family: "Arimo", Arial, sans-serif;
  }

  /* Back side */
  .card-back { background: var(--brand-blue); }
  .back-shapes { position: absolute; inset: 0; width: 100%; height: 100%; }
  .shape-deep { fill: var(--brand-blue-deep); }
  .back-name {
    position: absolute; left: 0; right: 0; top: 258px;
    text-align: center;
    font-family: "Montserrat", Arial, sans-serif;
    font-weight: 600; font-size: 58px; line-height: 1;
    color: var(--card-white);
    letter-spacing: 0.5px;
  }

  /* Front side */
  .card-front { background: var(--card-white); }
  .card-shapes { position: absolute; inset: 0; width: 100%; height: 100%; }
  .shape-blue { fill: var(--brand-blue); }
  .shape-grey { fill: var(--swoosh-grey); }
  .company-name {
    position: absolute; left: 62px; top: 82px;
    font-family: "Montserrat", Arial, sans-serif;
    font-weight: 600; font-size: 50px; line-height: 1.02;
    color: var(--brand-blue);
    letter-spacing: 0.5px;
  }
  .holder { position: absolute; left: 62px; top: 236px; color: var(--card-white); }
  .holder-name { font-size: 36px; letter-spacing: -0.5px; }
  .holder-role { font-size: 20px; margin-top: 4px; }
  .contact-list {
    position: absolute; right: 58px; top: 418px;
    list-style: none; text-align: right;
    color: var(--ink); font-size: 23px;
  }
  .contact-item { display: flex; justify-content: flex-end; align-items: center; gap: 14px; height: 40px; }
  .contact-icon { width: 24px; height: 24px; flex: none; }
  .contact-icon .icon-bg { fill: var(--brand-blue); }
  .contact-icon .icon-mark { fill: none; stroke: var(--card-white); stroke-width: 1.8; }
</style>
</head>
<body>
  <div class="card-slot card-slot--back">
    <div class="card-face card-back">
      <svg class="back-shapes" viewBox="0 0 1000 590" preserveAspectRatio="none" aria-hidden="true">
        <path class="shape-deep" d="M1000,330 L1000,590 L720,590 C800,480 900,390 1000,330 Z"/>
      </svg>
      <div class="back-name">Tarrow Construct Works</div>
    </div>
  </div>

  <div class="card-slot card-slot--front">
    <div class="card-face card-front">
      <svg class="card-shapes" viewBox="0 0 1000 590" preserveAspectRatio="none" aria-hidden="true">
        <path class="shape-blue" d="M0,0 L955,0 C700,22 350,32 0,36 Z"/>
        <path class="shape-blue" d="M0,228 L462,218 C300,330 130,450 0,545 Z"/>
        <path class="shape-grey" d="M0,590 L0,572 C190,420 520,150 905,12 C610,150 330,340 272,590 Z"/>
      </svg>

      <div class="company-name">Tarrow<br>Construct Works</div>

      <div class="holder">
        <div class="holder-name">Sample Name</div>
        <div class="holder-role">Owner</div>
      </div>

      <ul class="contact-list">
        <li class="contact-item">0472 913 046
          <svg class="contact-icon" viewBox="0 0 24 24"><rect class="icon-bg" width="24" height="24"/><rect class="icon-mark" x="8" y="4" width="8" height="16" rx="1.5"/></svg>
        </li>
        <li class="contact-item">admin@tarrowconstructworks.com.au
          <svg class="contact-icon" viewBox="0 0 24 24"><rect class="icon-bg" width="24" height="24"/><rect class="icon-mark" x="5" y="7" width="14" height="10"/><path class="icon-mark" d="M5,7 L12,13 L19,7"/></svg>
        </li>
        <li class="contact-item">www.tarrowconstructworks.com.au
          <svg class="contact-icon" viewBox="0 0 24 24"><rect class="icon-bg" width="24" height="24"/><circle class="icon-mark" cx="12" cy="12" r="7"/><path class="icon-mark" d="M5,12 H19 M12,5 C9,9 9,15 12,19 C15,15 15,9 12,5"/></svg>
        </li>
      </ul>
    </div>
  </div>
</body>
</html>
```